Launching new podcast and need artwork

we are two guys in our early 40's from east Texas who are starting a podcast around personal finance.

The title of the podcast will be "Ledger Gripes" and the subtitle will be "Financial hacks with Some Backroad Sense"

We own the company boundlessdaysplanning.example and will be using the podcast as a lead generation for our primary business of financial coaching.

Target Market(s)

Male 35-45 years old

Industry/Entity Type

Personal finance

Requirements
Nice to have
• Rugged or rustic feel would fit our personas

```html
<!DOCTYPE html>
<html lang="en">
<head>
<meta charset="utf-8">
<title>Ledger Gripes — Podcast Cover</title>
<link rel="stylesheet" href="https://fonts.googleapis.com/css2?family=Poppins:wght@700;800&family=Allura&display=swap">
<style>
  :root {
    --band-deep: #2c5283;
    --band-glow: #4f87c0;
    --title-white: #ffffff;
    --title-lime: #a8ff5a;
    --ink-navy: #2f465e;
    --script-blue: #4a8fd6;
    --floor-light: #f3f5f8;
    --floor-mid: #e2e7ee;
    --glass: #d9dee5;
    --gold: #c99a2e;
  }
  html, body {
    margin: 0;
    padding: 0;
    width: 1200px;
    height: 1200px;
    overflow: hidden;
    background: #ffffff;
  }
  .cover {
    display: block;
    width: 1200px;
    height: 1200px;
  }
  .title {
    font-family: "Poppins", sans-serif;
    font-weight: 800;
  }
  .title-top { fill: var(--title-white); }
  .title-bottom { fill: var(--title-lime); }
  .subtitle {
    font-family: "Poppins", sans-serif;
    font-weight: 700;
    fill: var(--ink-navy);
  }
  .subtitle-script {
    font-family: "Allura", cursive;
    fill: var(--script-blue);
  }
</style>
</head>
<body>
<svg class="cover" viewBox="0 0 1200 1200" xmlns="http://www.w3.org/2000/svg">
  <defs>
    <radialGradient id="bandGlow" cx="0.68" cy="1" r="0.75">
      <stop offset="0" stop-color="var(--band-glow)"/>
      <stop offset="1" stop-color="var(--band-deep)"/>
    </radialGradient>
    <linearGradient id="floorWash" x1="0" y1="0" x2="0" y2="1">
      <stop offset="0" stop-color="var(--floor-mid)"/>
      <stop offset="0.55" stop-color="var(--floor-light)"/>
      <stop offset="1" stop-color="var(--floor-mid)"/>
    </linearGradient>
    <linearGradient id="hourglassTone" x1="0" y1="0" x2="0" y2="1">
      <stop offset="0" stop-color="var(--glass)"/>
      <stop offset="0.35" stop-color="var(--gold)"/>
      <stop offset="0.55" stop-color="var(--glass)"/>
      <stop offset="0.8" stop-color="var(--gold)"/>
      <stop offset="1" stop-color="var(--glass)"/>
    </linearGradient>
  </defs>

  <rect class="backdrop" x="0" y="597" width="1200" height="603" fill="url(#floorWash)"/>
  <rect class="title-band" x="0" y="0" width="1200" height="597" fill="url(#bandGlow)"/>

  <text class="title title-top" x="84" y="292" font-size="252" textLength="1026" lengthAdjust="spacingAndGlyphs">LEDGER</text>
  <text class="title title-bottom" x="89" y="550" font-size="316" textLength="1035" lengthAdjust="spacingAndGlyphs">GRIPES</text>

  <text class="subtitle" x="94" y="689" font-size="55" textLength="535" lengthAdjust="spacingAndGlyphs">FINANCIAL HACKS</text>
  <text class="subtitle-script" x="88" y="800" font-size="110">with</text>
  <text class="subtitle" x="94" y="902" font-size="90">SOME</text>
  <text class="subtitle" x="94" y="1001" font-size="90">BACKROAD</text>
  <text class="subtitle" x="94" y="1101" font-size="90">SENSE</text>

  <rect class="hourglass-photo" role="img" aria-label="Photo of a glass hourglass filled with gold coins trickling from the top bulb to the bottom" x="793" y="565" width="255" height="577" rx="60" fill="url(#hourglassTone)" opacity="0.85"/>
</svg>
</body>
</html>
```